Velorin business card design

Design a business card for a cryptocurrency company that uses the attached logo. Some example business cards to give you guys a flavor of what we're looking for is given below (of course feel free to be creative):
https://www.plumcardhub.example/studio.aspx?template=4819265_KT3&ag=True&xnav=HSG_Design_Image&rd=1
https://www.plumcardhub.example/studio.aspx?template=3027514_KT3&ag=True&xnav=HSG_Design_Image&rd=1
The business card should be clean/simple and convey the company name, what we're about and the specific persons contact info. In terms of what we're about, we can have our name Velorin, with a line under it that says "Cryptocurrency visualization, analytics, and trading"
We want something futuristic looking but simple / clean.
The color scheme for the logo should be used.
The name of the person and their title should be editable, so we can use the business card design for multiple people.
(Please use the zip file to get the vector graphics and different image formats)

```html
<!DOCTYPE html>
<html lang="en">
<head>
<meta charset="utf-8">
<title>Velorin business card</title>
<link rel="stylesheet" href="https://fonts.googleapis.com/css2?family=Roboto:wght@400;500;700&family=Roboto+Condensed:wght@700&display=swap">
<style>
  :root {
    --page: #dedede;
    --paper: #f6f6f6;
    --navy: #0f1f38;
    --blue: #0a8fd6;
    --green: #12d67f;
    --teal: #12b6a0;
    --ink: #4a4a4a;
    --white: #ffffff;
  }
  html, body {
    margin: 0;
    padding: 0;
    width: 1200px;
    height: 960px;
    overflow: hidden;
    background: var(--page);
    font-family: "Roboto", Arial, sans-serif;
  }
  .card {
    position: absolute;
    width: 600px;
    height: 343px;
    overflow: hidden;
  }
  .card-front { left: 314px; top: 113px; background: var(--paper); }
  .card-back  { left: 311px; top: 472px; background: var(--navy); }

  .brand {
    position: absolute;
    right: 40px;
    top: 56px;
    display: flex;
    align-items: center;
    gap: 12px;
  }
  .brand-mark { width: 26px; height: 26px; background: var(--teal); }
  .brand-name {
    font-weight: 700;
    font-size: 36px;
    letter-spacing: 2px;
    color: var(--navy);
    line-height: 1;
  }

  .person { position: absolute; left: 38px; top: 174px; }
  .person-name {
    font-family: "Roboto Condensed", "Arial Narrow", sans-serif;
    font-weight: 700;
    font-size: 21px;
    color: var(--navy);
    margin: 0;
    line-height: 1;
  }
  .person-title {
    font-weight: 500;
    font-size: 15px;
    color: var(--blue);
    margin: 7px 0 0;
    line-height: 1;
  }
  .divider {
    position: absolute;
    left: 38px;
    top: 227px;
    width: 521px;
    height: 1px;
    background: var(--navy);
  }
  .contacts {
    position: absolute;
    left: 38px;
    top: 240px;
    margin: 0;
    padding: 0;
    list-style: none;
    font-size: 14px;
    color: var(--ink);
  }
  .contacts li { display: flex; align-items: center; height: 19.5px; }
  .contacts svg { width: 14px; height: 14px; margin-right: 8px; fill: var(--navy); }

  .footer-band { position: absolute; left: 0; bottom: 0; width: 600px; height: 38px; }
  .website {
    position: absolute;
    right: 40px;
    bottom: 12px;
    color: var(--white);
    font-size: 14px;
    letter-spacing: 3px;
  }

  .back-brand {
    position: absolute;
    left: 0;
    right: 0;
    top: 130px;
    text-align: center;
    font-weight: 700;
    font-size: 48px;
    letter-spacing: 4px;
    color: var(--green);
    line-height: 1;
  }
  .tagline {
    position: absolute;
    left: 0;
    right: 0;
    top: 285px;
    text-align: center;
    font-size: 15px;
    color: var(--white);
    margin: 0;
  }
</style>
</head>
<body>
  <section class="card card-front">
    <div class="brand">
      <span class="brand-mark"></span>
      <span class="brand-name">VELORIN</span>
    </div>

    <div class="person">
      <h1 class="person-name">DANIEL REYES</h1>
      <p class="person-title">CEO/FOUNDER</p>
    </div>
    <div class="divider"></div>

    <ul class="contacts">
      <li>
        <svg viewBox="0 0 24 24" aria-hidden="true"><path d="M6.6 10.8c1.4 2.8 3.8 5.1 6.6 6.6l2.2-2.2c.3-.3.7-.4 1-.2 1.1.4 2.3.6 3.6.6.6 0 1 .4 1 1V20c0 .6-.4 1-1 1C10.6 21 3 13.4 3 4c0-.6.4-1 1-1h3.5c.6 0 1 .4 1 1 0 1.3.2 2.5.6 3.6.1.3 0 .7-.2 1l-2.3 2.2z"/></svg>
        555 014 2738
      </li>
      <li>
        <svg viewBox="0 0 24 24" aria-hidden="true"><path d="M7 1h10c1.1 0 2 .9 2 2v18c0 1.1-.9 2-2 2H7c-1.1 0-2-.9-2-2V3c0-1.1.9-2 2-2zm0 3v14h10V4H7zm5 15.5a1 1 0 100 2 1 1 0 000-2z"/></svg>
        555 019 4460
      </li>
      <li>
        <svg viewBox="0 0 24 24" aria-hidden="true"><path d="M3 5h18c.6 0 1 .4 1 1v12c0 .6-.4 1-1 1H3c-.6 0-1-.4-1-1V6c0-.6.4-1 1-1zm9 7.5L20 7H4l8 5.5zM4 9v8h16V9l-8 5.5L4 9z"/></svg>
        daniel@velorin.com
      </li>
    </ul>

    <svg class="footer-band" viewBox="0 0 600 38" aria-hidden="true">
      <defs>
        <linearGradient id="accent-strip" x1="0" x2="1" y1="0" y2="0">
          <stop offset="0" stop-color="#0a7fd8"/>
          <stop offset="0.5" stop-color="#12d67f"/>
          <stop offset="1" stop-color="#0a8fd6"/>
        </linearGradient>
      </defs>
      <polygon points="0,24 343,24 333,38 0,38" fill="url(#accent-strip)"/>
      <polygon points="370,0 600,0 600,38 338,38" fill="#0f1f38"/>
    </svg>
    <span class="website">www.velorin.com</span>
  </section>

  <section class="card card-back">
    <div class="back-brand">VELORIN</div>
    <p class="tagline">Cryptocurrency visualization, analytics, &amp; trading</p>
  </section>
</body>
</html>
```